Visitenkarten-Design für architect i.a.
Aufgabenstellung
Logo ( Siehe Anhang)
scrinari
dessignader da construcziun aulta
maturitad professiunla
architect i.a.

```html
<!DOCTYPE html>
<html lang="rm">
<head>
<meta charset="utf-8">
<title>Torvel – Visitenkarte</title>
<link rel="stylesheet" href="https://fonts.googleapis.com/css2?family=Open+Sans:wght@400;600&display=swap">
<style>
  :root {
    --backdrop: #eeebe6;
    --card: #ffffff;
    --sky: #8fd3ee;
    --slate: #4e7582;
    --ink: #4f5559;
    --name-ink: #555d63;
    --on-slate: #e9f4f8;
  }
  * { box-sizing: border-box; margin: 0; padding: 0; }
  html, body { width: 1200px; height: 1200px; overflow: hidden; }
  body {
    background: var(--backdrop);
    font-family: "Open Sans", Arial, sans-serif;
    position: relative;
  }
  .card {
    position: absolute;
    top: 297px;
    width: 400px;
    height: 611px;
    background: var(--card);
    overflow: hidden;
  }
  .card--front { left: 158px; }
  .card--back { left: 624px; }

  .bar { position: absolute; }
  .bar--sky { background: var(--sky); }
  .bar--slate { background: var(--slate); }

  /* front */
  .front-bar-left  { left: 0; top: 130px; width: 110px; height: 13px; }
  .front-bar-right { left: 284px; top: 130px; width: 116px; height: 13px; }

  .brand {
    position: absolute;
    left: 0; right: 0; top: 176px;
    display: flex; align-items: center; justify-content: center; gap: 14px;
  }
  .brand__mark { width: 26px; height: 26px; background: var(--sky); }
  .brand__name {
    font-size: 60px; font-weight: 600; color: var(--name-ink);
    letter-spacing: 1px; line-height: 1;
  }
  .motto {
    position: absolute; left: 0; right: 0; top: 250px;
    text-align: center; font-size: 25px; color: var(--name-ink); line-height: 1;
  }
  .role-list {
    position: absolute; left: 0; right: 0; top: 316px;
    text-align: center; list-style: none;
    font-size: 21px; line-height: 33px; color: var(--ink);
  }
  .front-bar-long  { left: 0; top: 474px; width: 301px; height: 21px; }
  .front-bar-short { left: 321px; top: 474px; width: 28px; height: 21px; }

  /* back */
  .back-bar-slate { left: 0; top: 129px; width: 44px; height: 14px; }
  .back-bar-sky   { left: 60px; top: 129px; width: 340px; height: 14px; }
  .address {
    position: absolute; left: 0; right: 0; top: 275px;
    text-align: center; font-style: normal;
    font-size: 21px; line-height: 33px; color: var(--ink);
  }
  .back-band { left: 0; top: 474px; width: 400px; height: 21px; }
  .contact {
    position: absolute; left: 0; right: 0; top: 495px; bottom: 0;
    background: var(--slate);
    display: flex; flex-direction: column; align-items: center; justify-content: center; gap: 14px;
    font-size: 21px; color: var(--on-slate);
  }
  .contact__row { display: flex; align-items: center; gap: 8px; }
  .contact__icon { width: 20px; height: 20px; flex: none; }
</style>
</head>
<body>
  <section class="card card--front">
    <div class="bar bar--sky front-bar-left"></div>
    <div class="bar bar--slate front-bar-right"></div>
    <div class="brand">
      <span class="brand__mark"></span>
      <span class="brand__name">torvel</span>
    </div>
    <p class="motto">spazis per mintga di</p>
    <ul class="role-list">
      <li>Designer des Baues aulta</li>
      <li>Maturitad professiunla</li>
      <li>Architekt i.a.</li>
    </ul>
    <div class="bar bar--sky front-bar-long"></div>
    <div class="bar bar--sky front-bar-short"></div>
  </section>

  <section class="card card--back">
    <div class="bar bar--slate back-bar-slate"></div>
    <div class="bar bar--sky back-bar-sky"></div>
    <address class="address">
      Adresse<br>
      Torvel Kinst<br>
      Lindenmattweg 17<br>
      6005 Luzern
    </address>
    <div class="bar bar--sky back-band"></div>
    <div class="contact">
      <div class="contact__row">
        <svg class="contact__icon" viewBox="0 0 20 20" aria-hidden="true">
          <circle cx="10" cy="10" r="10" fill="#8fd3ee"/>
          <path d="M6.6 4.8c.4-.3 1-.2 1.2.2l1 1.9c.2.4.1.8-.2 1.1l-.7.6c.5 1.2 1.4 2.2 2.6 2.7l.6-.7c.3-.3.8-.4 1.1-.2l1.9 1c.4.2.5.8.2 1.2l-.7.9c-.4.5-1.1.7-1.7.5-3-1-5.3-3.3-6.3-6.3-.2-.6 0-1.3.5-1.7z" fill="#4e7582"/>
        </svg>
        <span>079 412 58 03</span>
      </div>
      <div class="contact__row">
        <svg class="contact__icon" viewBox="0 0 20 20" aria-hidden="true">
          <circle cx="10" cy="10" r="10" fill="#8fd3ee"/>
          <rect x="5" y="6.5" width="10" height="7" rx="1" fill="none" stroke="#4e7582" stroke-width="1.4"/>
          <path d="M5.4 7l4.6 3.6L14.6 7" fill="none" stroke="#4e7582" stroke-width="1.4"/>
        </svg>
        <span>torvelkinst@postfeld.ch</span>
      </div>
    </div>
  </section>
</body>
</html>
```